Web design for TRADEBACKS. A forex rebate platform website

I need a complete design for a forex rebate website called TRADEBACKS. The website will include the following pages:

- Homepage
- Broker Listing Page
- Broker Rebate Detail Page

Please review the attached file for detailed requirements and the content that needs to be designed.

Number of Pages Required

3 page

```html
<!DOCTYPE html>
<html lang="en">
<head>
<meta charset="utf-8">
<title>TradeBacks – Forex Rebates</title>
<link href="https://fonts.googleapis.com/css2?family=Inter:wght@400;500;600;700&display=swap" rel="stylesheet">
<style>
:root{
  --navy:#0a1a44;--blue:#0455fe;--blue-soft:#3478fc;--tint:#f2f7ff;--white:#fff;
  --canvas:#e5e9f1;--ink:#0a1a44;--muted:#5b6580;--line:#e3e8f2;--grey:#c6ccd7;
}
*{box-sizing:border-box;margin:0;padding:0}
html,body{width:1200px;height:3721px;overflow:hidden}
body{background:var(--canvas);font-family:Inter,sans-serif;color:var(--ink);position:relative}
.page{position:absolute;left:245px;top:260px;width:710px;height:3350px;background:var(--tint);overflow:hidden}
.abs{position:absolute}
.center{left:0;width:100%;text-align:center}
h2{font-size:20px;font-weight:500;letter-spacing:-.3px}
.sub{font-size:8px;color:var(--muted);line-height:1.5}
.logo{font-weight:600;font-size:13px;color:var(--blue);letter-spacing:-.2px}
.nav{top:0;left:0;width:100%;height:36px}
.nav .logo{position:absolute;left:15px;top:10px}
.nav .links{position:absolute;left:265px;top:13px;font-size:7px;color:var(--muted);display:flex;gap:16px}
.btn{display:inline-block;background:var(--blue);color:#fff;border-radius:10px;font-size:7px;font-weight:600;padding:5px 10px}
.nav .actions{position:absolute;right:15px;top:9px;display:flex;align-items:center;gap:8px;font-size:7px}
.hero{left:15px;top:36px;width:679px;height:365px;border-radius:6px;background:radial-gradient(ellipse at 78% 35%,#1f4fb0 0%,#12307a 35%,var(--navy) 75%);color:#fff;overflow:hidden}
.hero-art{right:0;top:0;width:330px;height:365px;background:linear-gradient(120deg,rgba(10,26,68,0) 0%,rgba(52,120,252,.25) 60%,rgba(10,26,68,.2) 100%)}
.hero h1{position:absolute;left:45px;top:52px;font-size:29px;font-weight:600;line-height:36px;letter-spacing:-.6px}
.hero h1 em{font-style:normal;color:var(--blue-soft)}
.hero p{position:absolute;left:45px;top:138px;font-size:8px;line-height:1.45;opacity:.85;width:300px}
.hero .cta{position:absolute;left:45px;top:190px;display:flex;gap:14px;align-items:center;font-size:7px;font-weight:600}
.stat{top:270px;width:131px;height:44px;border:1px solid rgba(255,255,255,.25);background:rgba(255,255,255,.08);border-radius:3px;padding:9px 10px}
.stat b{display:block;color:var(--blue-soft);font-size:11px;font-weight:600}
.stat span{font-size:7px}
.step{top:536px;width:183px;height:183px;background:#fff;border-radius:4px;padding:22px 17px;overflow:hidden}
.step.dark{background:var(--navy);color:#fff}
.ico{width:26px;height:26px;border-radius:50%;background:#e4ecfd;display:flex;align-items:center;justify-content:center}
.dark .ico{background:var(--blue)}
.step h3{font-size:11px;font-weight:500;margin:12px 0 6px}
.step p{font-size:7px;line-height:1.45;color:var(--muted)}
.dark p{color:#c8d2ea}
.num{position:absolute;left:20px;bottom:-24px;font-size:72px;font-weight:300;color:transparent;-webkit-text-stroke:1px #e3e8f2}
.dark .num{-webkit-text-stroke:1px #233a7a}
.tabs{top:846px;left:60px;display:flex;gap:8px;font-size:6.5px;color:var(--muted)}
.tab{padding:4px 8px;border-radius:9px;display:flex;gap:5px;align-items:center}
.tab.on{border:1px solid var(--blue);background:#fff;color:var(--ink)}
.tab i{font-style:normal;background:#e4e8f0;border-radius:6px;padding:1px 4px;font-size:5.5px}
.tab.on i{background:var(--navy);color:#fff}
.broker{width:134px;height:46px;background:#fff;border-radius:3px;padding:7px 8px;display:flex;gap:8px;align-items:center}
.bmark{width:26px;height:26px;border-radius:50%;background:#e7ecf5;flex:none}
.broker b{display:block;font-size:8px;font-weight:500}
.broker span{display:block;font-size:6px;color:var(--muted)}
.broker a{display:block;font-size:6px;color:var(--blue);text-decoration:none;margin-top:2px}
.calc{left:109px;top:1109px;width:476px;height:186px;background:#fff;border-radius:3px}
.calc .f{position:absolute;left:30px;font-size:6.5px;color:var(--muted)}
.seg{display:flex;gap:2px;margin-top:5px}
.seg span{border:1px solid var(--line);padding:2px 5px;font-size:5.5px;border-radius:2px}
.seg span.on{color:var(--blue)}
.slider{position:absolute;left:30px;width:196px;height:4px;border-radius:2px;background:#e4e8f0}
.slider i{position:absolute;left:0;top:0;height:4px;border-radius:2px;background:var(--blue)}
.slider b{position:absolute;top:-3px;width:10px;height:10px;border-radius:50%;background:var(--blue);border:2px solid #fff;box-shadow:0 0 0 1px var(--blue)}
.pill{position:absolute;right:250px;font-size:5.5px;border:1px solid var(--line);border-radius:2px;padding:1px 4px;color:var(--ink)}
.result{left:255px;top:11px;width:211px;height:164px;background:var(--navy);border-radius:3px;color:#fff;text-align:center;padding-top:24px}
.result small{font-size:8px;opacity:.8;display:block}
.result strong{display:block;font-size:21px;font-weight:600;margin:6px 0 20px}
.why{top:1412px;width:134px;height:101px;background:#fff;border-radius:3px;padding:20px 14px}
.why h3{font-size:9px;font-weight:500;margin:12px 0 5px}
.why p{font-size:6.5px;color:var(--muted)}
.oico{width:26px;height:24px}
.feed{height:46px;background:#fff;border-radius:3px;display:flex;align-items:center;padding:0 10px;gap:10px;overflow:hidden}
.fav{width:26px;height:26px;border-radius:50%;background:var(--navy);flex:none}
.fav.blue{background:var(--blue)}
.feed b{display:block;color:var(--blue);font-size:10px;font-weight:600}
.feed span{font-size:6.5px;color:var(--ink);white-space:nowrap}
.feed em{margin-left:auto;font-style:normal;font-size:5.5px;border:1px solid var(--line);border-radius:2px;padding:2px 4px;flex:none}
.band{left:0;width:100%;background:#fff}
.proof{top:1896px;width:185px;height:206px;background:#eef2f9;border-radius:3px;overflow:hidden}
.phone{position:absolute;left:30px;top:22px;width:125px;height:200px;border:4px solid #111;border-bottom:none;border-radius:16px 16px 0 0;background:#fff}
.phone .notch{position:absolute;left:38px;top:2px;width:40px;height:8px;border-radius:5px;background:#111}
.phone .app{position:absolute;left:8px;top:22px;font-size:5.5px;color:var(--blue);font-weight:600}
.phone .tick{position:absolute;left:50%;top:52px;margin-left:-9px;width:18px;height:18px;border-radius:50%;border:2px solid #2fb36b}
.phone .amt{position:absolute;left:0;width:100%;top:88px;text-align:center;font-size:11px;font-weight:700}
.phone .lbl{position:absolute;left:0;width:100%;top:104px;text-align:center;font-size:5px;color:var(--muted)}
.phone .row{position:absolute;left:10px;right:10px;height:1px;background:var(--line)}
.pay{top:2248px;left:0;width:100%;display:flex;justify-content:center;gap:70px;font-size:12px;font-weight:600;color:#b9c0cd}
.pay span{display:flex;align-items:center;gap:5px}
.pay i{width:12px;height:12px;border-radius:50%;background:var(--grey)}
.quote{top:2407px;width:183px;height:181px;background:#fff;border:1px solid var(--line);border-radius:3px;padding:22px 17px;overflow:hidden}
.stars{color:#f5a623;font-size:7px;letter-spacing:1px}
.quote p{font-size:7px;font-style:italic;color:var(--muted);line-height:1.55;margin-top:12px}
.who{position:absolute;left:17px;bottom:22px;display:flex;gap:8px;align-items:center}
.who i{width:20px;height:20px;border-radius:50%;background:#eef2f9}
.who b{display:block;font-size:7px;font-weight:500}
.who span{font-size:5.5px;color:var(--muted)}
.trust{right:60px;top:2376px;display:flex;align-items:center;gap:5px;font-size:6px}
.trust .badge{width:46px;height:8px;border-radius:2px;background:var(--grey)}
.faq{left:208px;width:278px;height:27px;background:#fff;border-radius:2px;display:flex;justify-content:space-between;align-items:center;padding:0 10px;font-size:7px}
.cta-band{left:8px;top:3004px;width:678px;height:187px;border-radius:5px;background:radial-gradient(ellipse at 80% 40%,#173a8c 0%,var(--navy) 65%);color:#fff;text-align:center}
.cta-band h2{margin-top:60px;font-size:22px}
.cta-band h2 em{font-style:normal;color:var(--blue-soft)}
.cta-band p{font-size:8px;opacity:.85;margin:8px 0 14px}
.foot{font-size:6.5px;line-height:2.1}
.foot small{color:var(--muted);font-size:5.5px;display:block}
.social{display:flex;gap:5px;justify-content:center;margin:4px 0}
.social i{width:7px;height:7px;border-radius:50%;background:var(--blue)}
</style>
</head>
<body>
<main class="page">

  <header class="abs nav">
    <span class="logo">TradeBacks</span>
    <nav class="links"><span>How It Works</span><span>Brokers</span><span>About</span><span>News</span></nav>
    <div class="actions"><span class="btn">Sign Up</span><span>Login</span><span style="color:var(--muted)">● EN</span></div>
  </header>

  <section class="abs hero">
    <div class="abs hero-art" role="img" aria-label="Glowing world map with candlestick chart"></div>
    <h1>Forex Rebates Made Simple.<br>Up to <em>90%</em> Back.</h1>
    <p>Earn higher rebates from the world's leading forex brokers without affecting your spreads, commissions, or trading conditions.</p>
    <div class="cta"><span class="btn" style="padding:6px 10px">Start Earning Rebates</span><span>Compare Brokers ↗</span></div>
    <div class="abs stat" style="left:45px"><b>$7.5M+</b><span>Rebates paid in total</span></div>
    <div class="abs stat" style="left:192px"><b>15,000+</b><span>Active Traders</span></div>
    <div class="abs stat" style="left:339px"><b>40+</b><span>Supported Brokers</span></div>
    <div class="abs stat" style="left:487px"><b>100K</b><span>Daily Payout Frequency</span></div>
  </section>

  <h2 class="abs" style="left:60px;top:452px">What is a Forex Rebate?</h2>
  <p class="abs sub" style="left:60px;top:488px;width:400px">Every trade generates spread or commission fees. Instead of letting those costs add up, TradeBacks returns a significant portion back to you as cashback rebates.</p>
  <article class="abs step" style="left:60px"><div class="ico"><svg width="12" height="12" viewBox="0 0 12 12"><path d="M1 10 4 6 7 8 11 2" stroke="#3478fc" fill="none" stroke-width="1.4"/></svg></div><h3>Trade As Usual</h3><p>Keep trading with your broker normally. No changes to your platform, spreads, or execution.</p><span class="num">01</span></article>
  <article class="abs step dark" style="left:256px"><div class="ico"><svg width="12" height="12" viewBox="0 0 12 12"><rect x="1" y="3" width="10" height="6" rx="1" stroke="#fff" fill="none"/></svg></div><h3>Broker Pays Us</h3><p>Your broker pays TradeBacks a commission for introducing you as a client of the platform.</p><span class="num">02</span></article>
  <article class="abs step" style="left:452px"><div class="ico"><svg width="12" height="12" viewBox="0 0 12 12"><circle cx="6" cy="6" r="4.5" stroke="#3478fc" fill="none" stroke-width="1.3"/></svg></div><h3>Get Cashback</h3><p>We share up to $50 per lot back with you through daily rebate payments.</p><span class="num">03</span></article>

  <h2 class="abs" style="left:60px;top:770px">Trusted Brokers</h2>
  <p class="abs sub" style="left:60px;top:806px">Selected brokers with competitive rebate terms and clear cashback value.</p>
  <div class="abs tabs">
    <span class="tab on">All Brokers <i>10</i></span><span class="tab">Daily Cash <i>12</i></span><span class="tab">Weekly Cash <i>10</i></span><span class="tab">Monthly Cash <i>10</i></span><span class="tab">EA Friendly <i>10</i></span><span class="tab">All Brokers <i>10</i></span><span class="tab">Scalping Fr. <i>10</i></span>
  </div>
  <div class="abs broker" style="left:60px;top:878px"><i class="bmark"></i><div><b>Harborline</b><span>Max. Rebate: 90%</span><a>Quick view</a></div></div>
  <div class="abs broker" style="left:207px;top:878px"><i class="bmark"></i><div><b>Norvale</b><span>Max. Rebate: 90%</span><a>Quick view</a></div></div>
  <div class="abs broker" style="left:353px;top:878px"><i class="bmark"></i><div><b>Quillstone</b><span>Max. Rebate: 90%</span><a>Quick view</a></div></div>
  <div class="abs broker" style="left:500px;top:878px"><i class="bmark"></i><div><b>Brightpath</b><span>Max. Rebate: 90%</span><a>Quick view</a></div></div>
  <div class="abs broker" style="left:133px;top:939px"><i class="bmark"></i><div><b>Kestrel Trade</b><span>Max. Rebate: 90%</span><a>Quick view</a></div></div>
  <div class="abs broker" style="left:281px;top:939px"><i class="bmark"></i><div><b>Alderon</b><span>Max. Rebate: 90%</span><a>Quick view</a></div></div>
  <div class="abs broker" style="left:428px;top:939px"><i class="bmark"></i><div><b>Milbrook</b><span>Max. Rebate: 90%</span><a>Quick view</a></div></div>

  <h2 class="abs center" style="top:1037px;font-size:22px">Calculate Your Cashback</h2>
  <p class="abs sub center" style="top:1074px">Simple rebate calculator to estimate your potential cashback</p>
  <section class="abs calc">
    <span class="abs" style="left:30px;top:26px;font-size:8px;font-weight:500">Forex Rebate Calculator</span>
    <div class="f" style="top:50px">Units<div class="seg"><span class="on">Pips</span><span>USD</span></div></div>
    <div class="f" style="top:50px;left:92px">Units<div class="seg"><span class="on">Pips</span><span>USD</span></div></div>
    <span class="f" style="top:96px">Trades per day</span><span class="pill" style="top:95px">25</span>
    <div class="slider" style="top:114px"><i style="width:48px"></i><b style="left:44px"></b></div>
    <span class="f" style="top:134px">Rebates</span><span class="pill" style="top:134px">0.70 Pips</span>
    <div class="slider" style="top:152px"><i style="width:30px"></i><b style="left:26px"></b></div>
    <div class="abs result"><small>Monthly Profit</small><strong>$3,675.00</strong><small>Yearly Profit</small><strong>$44,100.00</strong></div>
  </section>

  <h2 class="abs" style="left:60px;top:1346px">Why Choose TradeBacks</h2>
  <p class="abs sub" style="left:60px;top:1382px">Selected brokers with competitive rebate terms and clear cashback value.</p>
  <article class="abs why" style="left:60px"><svg class="oico" viewBox="0 0 26 24"><rect x="3" y="3" width="16" height="18" rx="1" stroke="#0455fe" fill="none" stroke-width="1.3"/><path d="M7 16V12M11 16V9M15 16V6" stroke="#0455fe" stroke-width="1.3"/></svg><h3>Real-Time Reports</h3><p>View earnings in real-time.</p></article>
  <article class="abs why" style="left:207px"><svg class="oico" viewBox="0 0 26 24"><path d="M3 20h18M6 20V12M11 20V8M16 20V4" stroke="#0455fe" fill="none" stroke-width="1.4"/></svg><h3>Highest Rates</h3><p>We pay the best rebate rates</p></article>
  <article class="abs why" style="left:354px"><svg class="oico" viewBox="0 0 26 24"><circle cx="14" cy="12" r="8" stroke="#0455fe" fill="none" stroke-width="1.3"/><path d="M14 7v10M11.5 9.5h4a1.5 1.5 0 0 1 0 3h-3a1.5 1.5 0 0 0 0 3h4" stroke="#0455fe" fill="none" stroke-width="1.1"/></svg><h3>Fast Payouts</h3><p>Get your rebates quickly</p></article>
  <article class="abs why" style="left:501px"><svg class="oico" viewBox="0 0 26 24"><circle cx="12" cy="13" r="7" stroke="#0455fe" fill="none" stroke-width="1.3"/><path d="M15 4h8v6h-4l-2 2v-2" stroke="#0455fe" fill="none" stroke-width="1.2"/></svg><h3>Awesome Support</h3><p>Get answers on time</p></article>

  <h2 class="abs center" style="top:1565px">Live Rebate Feed</h2>
  <div class="abs feed" style="left:-60px;top:1610px;width:107px"><em>Just Now</em></div>
  <div class="abs feed" style="left:60px;top:1610px;width:273px"><i class="fav"></i><div><b>$245.80</b><span>John (Indonesia) earned cashback from TradeBacks</span></div><em>Just Now</em></div>
  <div class="abs feed" style="left:354px;top:1610px;width:274px"><i class="fav blue"></i><div><b>$245.80</b><span>John (Indonesia) earned cashback from TradeBacks</span></div><em>Just Now</em></div>
  <div class="abs feed" style="left:647px;top:1610px;width:273px"><i class="fav"></i><div><b>$245.80</b><span>John (Indonesia) earned cashback</span></div></div>
  <div class="abs feed" style="left:-120px;top:1671px;width:265px"><span style="margin-left:auto">cashback from TradeBacks</span><em>Just Now</em></div>
  <div class="abs feed" style="left:162px;top:1671px;width:279px"><i class="fav"></i><div><b>$412.30</b><span>Michael (Thailand) earned cashback from TradeBacks</span></div><em>Just Now</em></div>
  <div class="abs feed" style="left:457px;top:1671px;width:279px"><i class="fav blue"></i><div><b>$245.80</b><span>John (Indonesia) earned cashback from TradeBacks</span></div><em>Just Now</em></div>

  <div class="abs band" style="top:1769px;height:383px"></div>
  <h2 class="abs center" style="top:1818px">Real Payout Proofs</h2>
  <p class="abs sub center" style="top:1854px">Every screenshot below is a genuine payment received by our traders.<br>No stock photos. No fake numbers.</p>
  <div class="abs proof" style="left:65px"><div class="phone"><i class="notch"></i><span class="app">Receipt</span><i class="tick"></i><div class="amt">0.085 CRX</div><div class="lbl">Transaction Successful</div><i class="row" style="top:130px"></i><i class="row" style="top:145px"></i><i class="row" style="top:160px"></i></div></div>
  <div class="abs proof" style="left:263px"><div class="phone"><i class="notch"></i><span class="app">Receipt</span><i class="tick"></i><div class="amt">$4,500.00</div><div class="lbl">Transfer Successful</div><i class="row" style="top:130px"></i><i class="row" style="top:160px"></i></div></div>
  <div class="abs proof" style="left:458px"><div class="phone"><i class="notch"></i><span class="app">Receipt</span><i class="tick"></i><div class="amt">1,250.00 USD</div><div class="lbl">Transaction Successful</div><i class="row" style="top:130px"></i><i class="row" style="top:150px"></i></div></div>

  <h2 class="abs center" style="top:2201px">Payment Methods</h2>
  <div class="abs pay"><span><i></i>Coinvale</span><span><i></i>Ledgra</span><span><i></i>Nodecash</span><span><i></i>Walletly</span></div>

  <div class="abs band" style="top:2310px;height:347px"></div>
  <h2 class="abs" style="left:60px;top:2359px">What Our Traders Say</h2>
  <div class="abs trust"><b>Excellent</b><i class="badge"></i><span>20,501 reviews on</span><b>Revuly</b></div>
  <article class="abs quote" style="left:-136px"><div class="stars">★★★★★</div><p>"I was pleasantly surprised to receive my $170 rebate payment in my Quickwallet account within 24 hours, even though the estimated processing time was 72 hours. Excellent service from TradeBacks - fast, professional, and dependable."</p></article>
  <article class="abs quote" style="left:60px"><div class="stars">★★★★★</div><p>"I was pleasantly surprised to receive my $170 rebate payment in my Quickwallet account within 24 hours, even though the estimated processing time was 72 hours. Excellent service from TradeBacks - fast, professional, and dependable."</p><div class="who"><i></i><div><b>Tomas Verlin</b><span>Revuly - Verified</span></div></div></article>
  <article class="abs quote" style="left:256px"><div class="stars">★★★★★</div><p>"I was pleasantly surprised to receive my $170 rebate payment in my Quickwallet account within 24 hours, even though the estimated processing time was 72 hours. Excellent service from TradeBacks - fast, professional, and dependable."</p><div class="who"><i></i><div><b>Tomas Verlin</b><span>Revuly - Verified</span></div></div></article>
  <article class="abs quote" style="left:452px"><div class="stars">★★★★★</div><p>"I was pleasantly surprised to receive my $170 rebate payment in my Quickwallet account within 24 hours, even though the estimated processing time was 72 hours. Excellent service from TradeBacks - fast, professional, and dependable."</p><div class="who"><i></i><div><b>Tomas Verlin</b><span>Revuly - Verified</span></div></div></article>
  <article class="abs quote" style="left:648px"><div class="stars">★★★★★</div><p>"I was pleasantly surprised to receive my $170 rebate payment in my Quickwallet account within 24 hours, even though the estimated processing time was 72 hours."</p><div class="who"><i></i><div><b>Tomas Verlin</b><span>Revuly</span></div></div></article>
  <div class="abs" style="left:60px;top:2604px;display:flex;gap:3px"><i style="width:4px;height:4px;border-radius:2px;background:var(--grey)"></i><i style="width:14px;height:4px;border-radius:2px;background:var(--blue)"></i><i style="width:4px;height:4px;border-radius:2px;background:var(--grey)"></i></div>

  <h2 class="abs center" style="top:2709px">From The FAQs</h2>
  <div class="abs faq" style="top:2748px"><span>What is Forex Rebate?</span><span>+</span></div>
  <div class="abs faq" style="top:2780px"><span>How does TradeBacks work?</span><span>+</span></div>
  <div class="abs faq" style="top:2813px"><span>Does it affect trading conditions?</span><span>+</span></div>
  <div class="abs faq" style="top:2845px"><span>When are rebates paid?</span><span>+</span></div>
  <div class="abs faq" style="top:2878px"><span>Which brokers are supported?</span><span>+</span></div>
  <div class="abs faq" style="top:2910px"><span>How do I withdraw earnings?</span><span>+</span></div>
  <p class="abs sub center" style="top:2946px;font-size:6px">Got other question? Ask us here</p>

  <section class="abs cta-band">
    <h2>Start <em>Earning</em> Forex Rebates Today</h2>
    <p>Join thousands of traders already receiving cashback from every trade.</p>
    <span class="btn" style="padding:7px 12px">Create Free Account</span>
  </section>

  <div class="abs foot" style="left:60px;top:3240px"><small>Company</small>About Us<br>Contact</div>
  <div class="abs foot" style="left:152px;top:3240px"><small>Resources</small>Brokers<br>Calculator<br>FAQ</div>
  <div class="abs foot" style="left:270px;top:3240px;width:150px;text-align:center;line-height:1.3">
    <span class="logo">TradeBacks</span>
    <div class="social"><i></i><i></i><i></i></div>
    <small>Risk Warning: Trading forex and CFDs involves significant risk and can result in the loss of your invested capital. © 2026 TradeBacks. All rights reserved.</small>
  </div>
  <div class="abs foot" style="left:490px;top:3240px"><small>Legal</small>Privacy Policy<br>Terms &amp; Conditions</div>
  <div class="abs foot" style="left:586px;top:3240px"><small>Information</small>Risk Disclaimer<br>Contact</div>

</main>
</body>
</html>
```